Responsive OnePage Design for recruitment company

BrightHire is a modern company that sources interim people for its customers. Mostly developers, scrum master, project managers and designers. In this website we want to tell something about us, about how we work, our customers and we want our candidates be able to subscribe. The subscription form should be several fields (name, surname, email address, phone number and the possibility to upload your resume.We want it to fit into a existing wordpress plugin. We also want a listing of our job opportunities. The listing should be designed in a clear readable overview and if you click on the job you should get the details and be able to respond quickly by filling in you name, surname, email address, rate, phone number and upload your resume. We want this to be a standard configurable plugin. It should be easy to fill in the jobs in Wordpress by our administrator. We want a fresh, modern and cool design. It should be a responsive onepage design. If you click on a listed job you should stay on the same page. Our logo is added.

Target Market(s)

recruitment

Industry/Entity Type

Recruitment

Font styles to use
Sans Serif

Colors

Designer to choose colors to be used in the design.

Requirements
Must have
• Onepage design
• listing of job opportunities
• subscription forms
• be responsive

```html
<!DOCTYPE html>
<html lang="en">
<head>
<meta charset="utf-8">
<title>BrightHire</title>
<link href="https://fonts.googleapis.com/css2?family=Montserrat:wght@300;400;500;600;700&display=swap" rel="stylesheet">
<style>
:root{
  --blue:#0e6fb6;
  --blue-dark:#0b5d9a;
  --ink:#222831;
  --text:#444;
  --muted:#9a9a9a;
  --line:#e6e6e6;
  --lavender:#ece9fb;
  --pink:#f28ad0;
  --band:#f7f7f8;
  --white:#fff;
}
*{box-sizing:border-box;margin:0;padding:0}
html,body{width:1200px;height:2922px;overflow:hidden}
body{position:relative;background:var(--white);font-family:'Montserrat',sans-serif;color:var(--text)}
.abs{position:absolute}
a{color:inherit;text-decoration:none}

/* header */
.brand{left:205px;top:16px;font-size:19px;letter-spacing:3px;color:var(--ink);font-weight:500}
.brand b{color:var(--blue);font-weight:500}
.nav{top:21px;font-size:11.5px;color:var(--ink)}
.search{left:740px;top:13px;width:130px;height:25px;border:1px solid #ccc;border-radius:3px;font-size:8px;padding:7px 10px;color:#666}
.search svg{position:absolute;right:8px;top:5px}
.register{left:938px;top:13px;width:60px;height:25px;border:1px solid var(--blue);border-radius:3px;font-size:11px;color:var(--blue);text-align:center;line-height:23px}
.header-line{left:205px;top:50px;width:795px;height:1px;background:#f0f0f0}

/* decorative blobs */
.blob-left{left:-80px;top:230px;width:175px;height:285px;border-radius:50%;background:var(--lavender);opacity:.7}
.blob-left2{left:-90px;top:1660px;width:130px;height:310px;border-radius:50%;background:var(--lavender);opacity:.7}
.blob-right{left:1100px;top:1610px;width:200px;height:330px;border-radius:50%;background:#fcf2f8}
.pink-dot{left:1187px;top:186px;width:26px;height:26px;border-radius:50%;background:var(--pink)}

/* hero form */
.hero-form{left:205px;top:118px;width:225px;height:317px;background:var(--blue);color:var(--white);padding:30px 25px;box-shadow:0 8px 20px rgba(14,111,182,.25)}
.hero-form h2{font-size:12.5px;font-weight:600;line-height:18px;margin-bottom:14px}
.hero-form .field{font-size:10px;border-bottom:1px solid rgba(255,255,255,.6);padding:4px 0 5px;margin-bottom:13px;width:175px}
.hero-form .upload{font-size:10px;text-decoration:underline;margin:18px 0 20px}
.hero-form .btn{display:inline-block;background:var(--white);color:var(--blue);font-size:10px;padding:6px 12px;border-radius:3px}
.hero-blob{left:845px;top:95px;width:240px;height:350px;border-radius:55% 45% 50% 50%;background:var(--lavender)}
.hero-art{left:560px;top:95px;width:360px;height:310px;border-radius:6px;background:linear-gradient(135deg,rgba(245,244,253,.9),rgba(226,230,245,.9))}
.dots{top:460px;width:7px;height:7px;border-radius:50%;background:#ddd}

.divider{left:205px;width:795px;height:1px;background:var(--line)}

/* about */
.eyebrow{left:207px;top:548px;font-size:10px;color:var(--blue)}
.about-title{left:205px;top:566px;font-size:14px;color:var(--ink)}
.about-copy{left:207px;top:602px;width:380px;font-size:10px;line-height:19px;color:var(--muted)}
.about-copy p{margin-bottom:18px}
.about-frame{left:770px;top:552px;width:228px;height:185px;border:11px solid var(--blue)}
.about-art{left:680px;top:585px;width:275px;height:210px;background:linear-gradient(160deg,#ffffff,#e8eef6);box-shadow:0 6px 20px rgba(0,0,0,.12);border-radius:8px}

/* filter + jobs */
.section-label{font-size:14px;color:var(--ink)}
.filter{left:205px;top:915px;width:225px;height:465px;background:var(--white);box-shadow:0 4px 16px rgba(0,0,0,.12);padding:25px 28px 0 30px}
.filter-item{display:flex;justify-content:space-between;font-size:9.5px;color:var(--muted);height:30px;align-items:center}
.filter-item i{width:4px;height:4px;border-radius:50%;background:var(--blue)}
.apply{display:inline-block;margin:40px 0 0 -2px;background:var(--blue);color:var(--white);font-size:11px;padding:6px 20px;border-radius:2px}

.job{left:447px;width:551px;background:var(--white);box-shadow:0 4px 16px rgba(0,0,0,.12)}
.job .icon{position:absolute;left:18px;top:18px}
.job h3{position:absolute;left:133px;top:17px;font-size:14px;font-weight:500;color:var(--ink)}
.job .desc{position:absolute;left:133px;top:43px;width:395px;font-size:10px;line-height:17px;color:var(--text)}
.job .meta{position:absolute;left:133px;top:80px;font-size:9px;color:#c8c8c8}
.job .details{position:absolute;left:135px;top:102px;font-size:10px;color:var(--blue);font-weight:600}

.apply-pop{left:605px;top:1062px;width:227px;height:318px;background:var(--white);box-shadow:0 6px 20px rgba(0,0,0,.18);padding:34px 25px 0 27px}
.apply-pop .field{font-size:9.5px;color:var(--muted);border-bottom:1px solid var(--line);padding-bottom:6px;margin-bottom:18px}
.apply-pop .upload{font-size:10px;color:var(--blue);text-decoration:underline;margin:4px 0 20px}
.apply-pop .btn{display:inline-block;background:var(--blue);color:var(--white);font-size:10px;padding:7px 20px;border-radius:2px}

.load-more{left:447px;top:1565px;font-size:11px;font-weight:700;color:var(--blue)}

/* recent jobs */
.recent{width:225px;height:187px;top:1698px;background:var(--white);box-shadow:0 4px 16px rgba(0,0,0,.12);padding:20px 16px}
.recent h4{font-size:13px;font-weight:500;color:var(--blue);margin-bottom:14px}
.recent li{list-style:none;display:flex;align-items:center;gap:9px;font-size:9.5px;color:var(--muted);height:23px}
.arrow{top:1780px}

/* testimonial */
.avatar{left:237px;top:2030px;width:63px;height:63px;border-radius:50%;background:linear-gradient(135deg,#d9cfc6,#8a7566)}
.quote{left:328px;top:2040px;width:450px;font-size:11px;line-height:17px;color:var(--ink)}
.quote small{display:block;font-size:8px;color:#666;margin-top:10px}

/* newsletter */
.band{left:0;top:2157px;width:1200px;height:248px;background:var(--band)}
.news-title{left:0;width:1200px;top:2230px;text-align:center;font-size:14px;color:var(--ink)}
.news-sub{left:0;width:1200px;top:2252px;text-align:center;font-size:9.5px;color:#aaa}
.news-input{left:390px;top:2300px;width:420px;height:43px;background:var(--white);box-shadow:0 4px 16px rgba(0,0,0,.1);font-size:10px;color:#aaa;padding:15px 16px}
.news-btn{left:765px;top:2300px;width:45px;height:43px;background:var(--blue);display:flex;align-items:center;justify-content:center}

/* companies */
.company{width:160px;height:66px;border:1px solid var(--line);display:flex;align-items:center;justify-content:center;gap:6px;font-size:11px;font-weight:600;color:var(--ink)}
.company i{width:10px;height:10px;background:var(--blue)}

/* footer */
.footer{left:0;top:2720px;width:1200px;height:187px;background:var(--blue);color:var(--white)}
.footer-brand{top:36px;width:1200px;text-align:center;font-size:18px;letter-spacing:3px;font-weight:500}
.footer-links{top:80px;width:1200px;display:flex;justify-content:center;gap:36px;font-size:10px}
.social{top:124px;width:1200px;display:flex;justify-content:center;gap:10px}
.social i{width:8px;height:8px;border-radius:50%;background:var(--white)}
.copyright{left:0;top:2907px;width:1200px;text-align:center;font-size:7px;color:#555}
</style>
</head>
<body>

<!-- header -->
<div class="abs brand">BRIGHT<b>HIRE</b></div>
<a class="abs nav" style="left:440px">About us</a>
<a class="abs nav" style="left:503px">Our Work <svg width="8" height="6" viewBox="0 0 8 6"><path d="M1 1l3 3 3-3" fill="none" stroke="#555"/></svg></a>
<a class="abs nav" style="left:585px">Our Customers</a>
<div class="abs search">JOB SEARCH<svg width="13" height="13" viewBox="0 0 13 13"><circle cx="5.5" cy="5.5" r="4" fill="none" stroke="#666" stroke-width="1.3"/><path d="M8.5 8.5l3.5 3.5" stroke="#666" stroke-width="1.3"/></svg></div>
<a class="abs nav" style="left:895px;top:20px">Sign in</a>
<a class="abs register">Register</a>
<div class="abs header-line"></div>

<div class="abs blob-left"></div>
<div class="abs pink-dot"></div>

<!-- hero -->
<form class="abs hero-form">
  <h2>To manage your job search subscribe it now.</h2>
  <div class="field">Name</div>
  <div class="field">Sur Name</div>
  <div class="field">Email Address</div>
  <div class="field">Phone Number</div>
  <div class="upload">Upload Your Resume</div>
  <span class="btn">Subscribe</span>
</form>
<div class="abs hero-blob"></div>
<div class="abs hero-art" role="img" aria-label="Illustration of a team of three people working together at a desk with laptops"></div>
<span class="abs dots" style="left:618px"></span>
<span class="abs dots" style="left:630px;background:var(--pink)"></span>
<span class="abs dots" style="left:642px"></span>

<div class="abs divider" style="top:515px"></div>

<!-- about -->
<div class="abs eyebrow">About</div>
<h2 class="abs about-title" style="font-weight:400">BrightHire</h2>
<div class="abs about-copy">
  <p>Lorem Ipsum is simply dummy text of the printing and typesetting industry. Lorem Ipsum has been the industry's standard dummy text ever since the 1500s, when an unknown printer took a galley of type and scrambled it to make a type specimen book. It has survived not only five centuries, but also the leap into electronic typesetting, remaining essentially unchanged.</p>
  <p>It was popularised in the 1960s with the release of Lettermark sheets containing Lorem Ipsum passages, and more recently with desktop publishing software like LayoutPro including versions of Lorem Ipsum.</p>
</div>
<div class="abs about-frame"></div>
<div class="abs about-art" role="img" aria-label="Tablet and phone showing the job dashboard screens"></div>

<div class="abs divider" style="top:832px"></div>

<!-- filter -->
<h3 class="abs section-label" style="left:210px;top:882px;font-weight:400">Filter</h3>
<h3 class="abs section-label" style="left:457px;top:882px;font-weight:400">Popular job Category</h3>
<aside class="abs filter">
  <div class="filter-item">Location<i></i></div>
  <div class="filter-item">Job Function<i></i></div>
  <div class="filter-item">Skills Areas<i></i></div>
  <div class="filter-item">Education Level<i></i></div>
  <div class="filter-item">Professional Level<i></i></div>
  <div class="filter-item">Full Time / Part Time<i></i></div>
  <div class="filter-item">Remote / On Site<i></i></div>
  <div class="filter-item">Org Type<i></i></div>
  <span class="apply">Apply</span>
</aside>

<!-- job list -->
<article class="abs job" style="top:915px;height:140px">
  <svg class="icon" width="64" height="52" viewBox="0 0 64 52"><rect x="8" y="4" width="48" height="32" rx="2" fill="none" stroke="#333" stroke-width="1.6"/><path d="M2 40h60l-3 6H5z" fill="none" stroke="#333" stroke-width="1.6"/><circle cx="32" cy="20" r="9" fill="none" stroke="var(--blue)" stroke-width="1.5"/><path d="M29 17l-3 3 3 3M35 17l3 3-3 3" fill="none" stroke="var(--blue)" stroke-width="1.3"/></svg>
  <h3>Developers</h3>
  <p class="desc">Lorem Ipsum is simply dummy text of the printing and typesetting industry. Lorem Ipsum of type and scrambled it to make a type specimen book.</p>
  <span class="meta">Daniel Brook, March 6, 2019</span>
  <a class="details">Details</a>
</article>
<article class="abs job" style="top:1072px;height:128px">
  <svg class="icon" width="64" height="52" viewBox="0 0 64 52"><rect x="8" y="4" width="48" height="32" rx="2" fill="none" stroke="#333" stroke-width="1.6"/><path d="M2 40h60l-3 6H5z" fill="none" stroke="#333" stroke-width="1.6"/><circle cx="32" cy="20" r="9" fill="none" stroke="var(--blue)" stroke-width="1.5"/><circle cx="32" cy="18" r="3" fill="none" stroke="var(--blue)" stroke-width="1.3"/></svg>
  <h3>Scrum Master</h3>
  <p class="desc">Lorem Ipsum is simply dummy text of the printing and typesetting industry. Lorem Ipsum of type and scrambled it to make a type specimen book.</p>
  <span class="meta">Daniel Brook, March 6, 2019</span>
  <a class="details" style="top:102px">Details</a>
</article>
<article class="abs job" style="top:1225px;height:130px">
  <svg class="icon" width="64" height="52" viewBox="0 0 64 52"><rect x="8" y="4" width="48" height="32" rx="2" fill="none" stroke="#333" stroke-width="1.6"/><path d="M2 40h60l-3 6H5z" fill="none" stroke="#333" stroke-width="1.6"/><circle cx="32" cy="20" r="9" fill="none" stroke="var(--blue)" stroke-width="1.5"/><rect x="28" y="17" width="8" height="6" fill="none" stroke="var(--blue)" stroke-width="1.3"/></svg>
  <h3>Project Managers</h3>
  <p class="desc">Lorem Ipsum is simply dummy text of the printing and typesetting industry. Lorem Ipsum of type and scrambled it to make a type specimen book.</p>
  <span class="meta">Daniel Brook, March 6, 2019</span>
  <a class="details" style="top:100px">Details</a>
</article>
<article class="abs job" style="top:1378px;height:130px">
  <svg class="icon" width="64" height="52" viewBox="0 0 64 52"><rect x="8" y="4" width="48" height="32" rx="2" fill="none" stroke="#333" stroke-width="1.6"/><path d="M2 40h60l-3 6H5z" fill="none" stroke="#333" stroke-width="1.6"/><circle cx="32" cy="20" r="9" fill="none" stroke="var(--blue)" stroke-width="1.5"/><path d="M32 14v12M28 18h8" stroke="var(--blue)" stroke-width="1.3"/></svg>
  <h3>Designers</h3>
  <p class="desc">Lorem Ipsum is simply dummy text of the printing and typesetting industry. Lorem Ipsum of type and scrambled it to make a type specimen book.</p>
  <span class="meta">Daniel Brook, March 6, 2019</span>
  <a class="details">Details</a>
</article>

<!-- quick apply -->
<svg class="abs" style="left:598px;top:1025px" width="20" height="24" viewBox="0 0 20 24"><path d="M6 2v12l-3-2-2 2 6 8h9l2-9-7-2V2z" fill="#fff" stroke="#222" stroke-width="1.3"/></svg>
<form class="abs apply-pop">
  <div class="field">Name</div>
  <div class="field">Sur Name</div>
  <div class="field">Email Address</div>
  <div class="field">Rate</div>
  <div class="field">Phone Number</div>
  <div class="upload">Upload Your Resume</div>
  <span class="btn">Submit</span>
</form>

<a class="abs load-more">Load More »</a>

<div class="abs divider" style="top:1625px"></div>

<!-- recent -->
<div class="abs blob-left2"></div>
<div class="abs blob-right"></div>
<h3 class="abs section-label" style="left:205px;top:1662px;font-weight:400">Recently posted jobs</h3>
<svg class="abs arrow" style="left:203px" width="12" height="18" viewBox="0 0 12 18"><path d="M9 2L3 9l6 7" fill="none" stroke="#333" stroke-width="1.6"/></svg>
<svg class="abs arrow" style="left:985px" width="12" height="18" viewBox="0 0 12 18"><path d="M3 2l6 7-6 7" fill="none" stroke="#333" stroke-width="1.6"/></svg>

<section class="abs recent" style="left:243px">
  <h4>Developers</h4>
  <ul>
    <li><svg width="12" height="10"><rect x="1" y="1" width="10" height="8" fill="none" stroke="#888"/><circle cx="6" cy="5" r="2" fill="#888"/></svg>Competitive</li>
    <li><svg width="12" height="12"><path d="M6 11C2 6 2 5 2 4a4 4 0 018 0c0 1 0 2-4 7z" fill="none" stroke="#888"/></svg>New York, NY, United States</li>
    <li><svg width="12" height="12"><circle cx="6" cy="6" r="5" fill="none" stroke="#888"/><path d="M6 3v3h3" fill="none" stroke="#888"/></svg>Permanent, Full Time</li>
    <li><svg width="12" height="12"><path d="M1 11h10M2 11V5h3v6M6 11V2h4v9" fill="none" stroke="#888"/></svg>Hudson Mutual Insurance Company</li>
    <li><svg width="12" height="12"><rect x="1" y="2" width="10" height="9" fill="none" stroke="#888"/><path d="M1 5h10" stroke="#888"/></svg>05 Mar 19</li>
  </ul>
</section>
<section class="abs recent" style="left:488px">
  <h4>Scrum Master</h4>
  <ul>
    <li><svg width="12" height="10"><rect x="1" y="1" width="10" height="8" fill="none" stroke="#888"/><circle cx="6" cy="5" r="2" fill="#888"/></svg>Competitive</li>
    <li><svg width="12" height="12"><path d="M6 11C2 6 2 5 2 4a4 4 0 018 0c0 1 0 2-4 7z" fill="none" stroke="#888"/></svg>New York, NY, United States</li>
    <li><svg width="12" height="12"><circle cx="6" cy="6" r="5" fill="none" stroke="#888"/><path d="M6 3v3h3" fill="none" stroke="#888"/></svg>Permanent, Full Time</li>
    <li><svg width="12" height="12"><path d="M1 11h10M2 11V5h3v6M6 11V2h4v9" fill="none" stroke="#888"/></svg>Hudson Mutual Insurance Company</li>
    <li><svg width="12" height="12"><rect x="1" y="2" width="10" height="9" fill="none" stroke="#888"/><path d="M1 5h10" stroke="#888"/></svg>05 Mar 19</li>
  </ul>
</section>
<section class="abs recent" style="left:732px">
  <h4>Project Managers</h4>
  <ul>
    <li><svg width="12" height="10"><rect x="1" y="1" width="10" height="8" fill="none" stroke="#888"/><circle cx="6" cy="5" r="2" fill="#888"/></svg>Competitive</li>
    <li><svg width="12" height="12"><path d="M6 11C2 6 2 5 2 4a4 4 0 018 0c0 1 0 2-4 7z" fill="none" stroke="#888"/></svg>New York, NY, United States</li>
    <li><svg width="12" height="12"><circle cx="6" cy="6" r="5" fill="none" stroke="#888"/><path d="M6 3v3h3" fill="none" stroke="#888"/></svg>Permanent, Full Time</li>
    <li><svg width="12" height="12"><path d="M1 11h10M2 11V5h3v6M6 11V2h4v9" fill="none" stroke="#888"/></svg>Hudson Mutual Insurance Company</li>
    <li><svg width="12" height="12"><rect x="1" y="2" width="10" height="9" fill="none" stroke="#888"/><path d="M1 5h10" stroke="#888"/></svg>05 Mar 19</li>
  </ul>
</section>

<div class="abs divider" style="top:1952px"></div>

<!-- testimonial -->
<h3 class="abs section-label" style="left:205px;top:1987px;font-weight:400">Our customers Says About us</h3>
<div class="abs avatar" role="img" aria-label="Portrait photo of the customer quoted"></div>
<blockquote class="abs quote">"With feedback coming from all directions, BrightHire helps store and organize it all.<br>Simpler review process for faster product decisions!"<small>Mara Ellison — User Research Coordinator at Lumo</small></blockquote>

<!-- newsletter -->
<div class="abs band"></div>
<svg class="abs" style="left:583px;top:2185px" width="34" height="34" viewBox="0 0 34 34"><path d="M3 14l14-10 14 10v17H3z" fill="none" stroke="var(--blue)" stroke-width="2"/><rect x="8" y="9" width="18" height="13" fill="#fff" stroke="var(--blue)" stroke-width="2"/><path d="M3 14l14 10 14-10" fill="none" stroke="var(--blue)" stroke-width="2"/></svg>
<h3 class="abs news-title" style="font-weight:400">Newsletter</h3>
<p class="abs news-sub">Subscribe Our Newsletter for latest news and update</p>
<div class="abs news-input">Email Id</div>
<div class="abs news-btn"><svg width="18" height="16" viewBox="0 0 18 16"><path d="M1 1l16 7-16 7 3-7z M4 8h13" fill="none" stroke="#fff" stroke-width="1.5"/></svg></div>

<!-- companies -->
<h3 class="abs section-label" style="left:205px;top:2450px;font-weight:400">Job By Company</h3>
<div class="abs company" style="left:248px;top:2505px">Northwind Tech</div>
<div class="abs company" style="left:428px;top:2505px"><i></i>Harborline</div>
<div class="abs company" style="left:605px;top:2505px">Elmfield Partners</div>
<div class="abs company" style="left:782px;top:2505px"><i></i>Bluepoint</div>
<div class="abs company" style="left:248px;top:2590px">Crestmoor Capital</div>
<div class="abs company" style="left:428px;top:2590px">Ridgeway Trust</div>
<div class="abs company" style="left:605px;top:2590px">Halvard &amp; Co</div>
<div class="abs company" style="left:782px;top:2590px">Stonebay</div>

<!-- footer -->
<footer class="abs footer">
  <div class="abs footer-brand">BRIGHTHIRE</div>
  <nav class="abs footer-links"><a>About Us</a><a>Site Map</a><a>Terms of Use</a><a>Privacy Policy</a><a>Contact Us</a><a>Job Seeker Sign In</a></nav>
  <div class="abs social"><i></i><i></i><i></i></div>
</footer>
<p class="abs copyright">© 2019 BRIGHTHIRE. All rights reserved.</p>

</body>
</html>
```